business card with logo Velmora Nails & Spa 2816 SW Quillan Ave Portland OR 97384

Would like to have a business card with our logo.
like bottle of polish with our logo or letter V on it
want something that first glance would let you know that it is a nail salon.
like the hands with polish bottle dripping.
like black or White back ground

Velmora Nails & Spa
(The Velvet Retreat)
2816 SW Quillan Ave
Portland, OR 97384
Call or Text: 1-503-555-0148
www.VelmoraNailsnSpa.example
Open 7 days a week.
After 7:00 PM is by appointment only.
Closed only on Thanksgiving & Christmas.

Target Market(s)

20%Man and 80%Woman 13-70

Industry/Entity Type

Business

Contact Information for Business Card

Elegant with Logo-Business name- address-phone-open days. closed day.

Font styles to use
Decorative
Script

Colors
000000

Requirements
Must have
• Logo and place for Technician Name
• Velmora Nails & Spa
• (The Velvet Retreat)
• 2816 SW Quillan Ave
• Portland, OR 97384
• Call or Text: 1-503-555-0148
• Open 7 days a week
• Closed only on Thanksgiving & Christmas.
• We accepted all major credit cards but prefer cash. Thank you
Nice to have
• Nail polish bottle with our Logo or letter V
Should not have
• too colorful

```html
<!DOCTYPE html>
<html lang="en">
<head>
<meta charset="utf-8">
<title>Velmora Nails &amp; Spa – Business Card</title>
<link rel="stylesheet" href="https://fonts.googleapis.com/css2?family=Open+Sans:wght@400;600&display=swap">
<style>
  :root {
    --ink: #1a1a1a;
    --muted: #3a3a3a;
    --accent: #9cc43b;
    --card-top: #ffffff;
    --card-bottom: #e6e6e6;
    --stage: #efefef;
    --skin-light: #f6dccd;
    --skin-mid: #efc3ad;
    --polish: #e66fa0;
  }
  * { box-sizing: border-box; margin: 0; padding: 0; }
  html, body { width: 1200px; height: 1023px; overflow: hidden; }
  body {
    background: var(--stage);
    font-family: "Open Sans", Arial, sans-serif;
    color: var(--ink);
    position: relative;
  }
  .card {
    position: absolute;
    left: 220px;
    width: 760px;
    height: 434px;
    border-radius: 22px;
    background: linear-gradient(160deg, var(--card-top) 0%, var(--card-bottom) 100%);
    box-shadow: 0 10px 30px rgba(0,0,0,.18);
    overflow: hidden;
  }
  .card--front { top: 50px; }
  .card--back { top: 539px; }

  /* front */
  .brand {
    position: absolute;
    left: 56px;
    top: 62px;
  }
  .brand__name {
    font-size: 62px;
    font-weight: 600;
    letter-spacing: -1px;
    line-height: 1;
  }
  .brand__sub {
    font-size: 26px;
    font-weight: 400;
    color: var(--accent);
    margin-top: 6px;
    display: flex;
    align-items: center;
    gap: 10px;
  }
  .brand__sub::before {
    content: "";
    width: 40px; height: 2px;
    background: var(--ink);
  }
  .brand__tagline {
    font-size: 19px;
    margin-top: 6px;
    color: var(--muted);
  }
  .contact {
    position: absolute;
    right: 48px;
    top: 58px;
    width: 330px;
    font-size: 16px;
    line-height: 1.55;
    color: var(--muted);
  }
  .contact__row {
    display: flex;
    justify-content: space-between;
    align-items: flex-start;
    gap: 10px;
  }
  .contact__icon { width: 15px; height: 15px; margin-top: 5px; flex: none; }
  .contact__rule {
    height: 1px;
    background: #b5b5b5;
    margin: 14px 0 12px;
  }
  .hours__row {
    display: flex;
    justify-content: space-between;
    align-items: center;
    font-size: 15.5px;
  }
  .hours__dot {
    width: 6px; height: 6px; border-radius: 50%;
    background: var(--accent); flex: none;
  }
  .visual-hands {
    position: absolute;
    left: 0; bottom: 0;
    width: 380px; height: 190px;
    background: linear-gradient(100deg, var(--skin-light) 0%, var(--skin-mid) 55%, rgba(239,195,173,0) 100%);
  }
  .visual-bottle {
    position: absolute;
    left: 370px; bottom: 40px;
    width: 110px; height: 150px;
    border-radius: 14px;
    background: linear-gradient(180deg, #9a9a9a 0%, #9a9a9a 40%, var(--polish) 40%, #f39bbd 100%);
  }

  /* back */
  .mark {
    position: absolute;
    left: 0; right: 0; top: 120px;
    text-align: center;
  }
  .mark__name {
    font-size: 92px;
    font-weight: 600;
    letter-spacing: -2px;
    line-height: 1;
  }
  .mark__sub {
    font-size: 34px;
    color: var(--accent);
    margin-top: 8px;
  }
  .payments {
    position: absolute;
    left: 40px; right: 40px; bottom: 34px;
    display: flex;
    align-items: center;
    gap: 22px;
    font-size: 14px;
  }
  .payments__note { flex: 1; text-align: right; color: var(--muted); }
  .pay {
    display: flex; align-items: center; gap: 5px;
    font-weight: 600; font-size: 13px; color: var(--ink);
  }
  .pay__chip { width: 10px; height: 10px; background: #888; }
</style>
</head>
<body>

<section class="card card--front" aria-label="Card front">
  <div class="brand">
    <div class="brand__name">Velmora</div>
    <div class="brand__sub">Nails n Spa</div>
    <div class="brand__tagline">The Velvet Retreat</div>
  </div>

  <div class="contact">
    <div class="contact__row">
      <span>2816 SW Quillan Ave<br>Portland, OR 97384</span>
      <svg class="contact__icon" viewBox="0 0 16 16"><path d="M8 1a5 5 0 0 0-5 5c0 4 5 9 5 9s5-5 5-9a5 5 0 0 0-5-5zm0 7a2 2 0 1 1 0-4 2 2 0 0 1 0 4z" fill="#9cc43b"/></svg>
    </div>
    <div class="contact__row">
      <span>1-503-555-0148</span>
      <svg class="contact__icon" viewBox="0 0 16 16"><circle cx="8" cy="8" r="7" fill="none" stroke="#9cc43b" stroke-width="1.5"/><path d="M5.5 4.5l1.5 1.5-.8 1a5 5 0 0 0 2.8 2.8l1-.8 1.5 1.5-1 1c-3 0-6-3-6-6z" fill="#9cc43b"/></svg>
    </div>
    <div class="contact__row">
      <span>www.VelmoraNailsnSpa.example</span>
      <svg class="contact__icon" viewBox="0 0 16 16"><circle cx="8" cy="8" r="7" fill="none" stroke="#9cc43b" stroke-width="1.5"/><path d="M1 8h14M8 1c3 3 3 11 0 14M8 1c-3 3-3 11 0 14" fill="none" stroke="#9cc43b" stroke-width="1.2"/></svg>
    </div>
    <div class="contact__rule"></div>
    <div class="hours__row"><span>Open 7 days a week.</span><span class="hours__dot"></span></div>
    <div class="hours__row"><span>Closed only on Thanksgiving &amp; Christmas</span><span class="hours__dot"></span></div>
  </div>

  <div class="visual-hands" role="img" aria-label="Photo of two hands with pink painted nails"></div>
  <div class="visual-bottle" role="img" aria-label="Photo of an open pink nail polish bottle"></div>
</section>

<section class="card card--back" aria-label="Card back">
  <div class="mark">
    <div class="mark__name">Velmora</div>
    <div class="mark__sub">Nails n Spa</div>
  </div>
  <div class="payments">
    <span class="pay"><span class="pay__chip"></span>Cardvia</span>
    <span class="pay"><span class="pay__chip"></span>Paymerge</span>
    <span class="pay"><span class="pay__chip"></span>Amerilink</span>
    <span class="pay"><span class="pay__chip"></span>Findpay</span>
    <span class="payments__note">We accepted all major credit cards but prefer cash</span>
  </div>
</section>

</body>
</html>
```